Rebrand of 3 bottle labels for nail polish brand

The task is to make a rebranding of our current gel nail polish bottle design. We have become one of the leading european nail polish brand, so we want to improve the quality of the label design to a more scandinavian and minimalistic bottle design, which stille has to be recognisable and unique.

We have attached a more detailed description of the rebranding instructions for our gel polish bottles called "bottle task".
Updates

The Labels should not be just Black and White as stated. But should be mainly Black and White and then some of our color as explained in the uploaded file.

Target Market(s)

Girls and women age 18-55 Northern Europe

Industry/Entity Type

Cosmetic/ Nail Gel Polish

Colors

Designer to choose only greyscale colors for use in the design.

Requirements
Must have
• See attched design instruction
Nice to have
• Moderne, Minimalist, Recognizable and Unique look
Should not have
• Too many elements, too busy design

```html
<!DOCTYPE html>
<html lang="en">
<head>
<meta charset="utf-8">
<title>Solvind bottle labels</title>
<link href="https://fonts.googleapis.com/css2?family=Barlow+Condensed:wght@400;500;600&family=Barlow:wght@400;600;700&family=Jost:wght@300;400;500&display=swap" rel="stylesheet">
<style>
  :root {
    --ink: #000;
    --paper: #fff;
    --rose: #c49a90;
    --red: #b01f24;
    --pattern: #3a3a3a;
  }
  * { margin: 0; padding: 0; box-sizing: border-box; }
  html, body { width: 900px; height: 1200px; overflow: hidden; background: var(--paper); }
  .canvas { position: relative; width: 900px; height: 1200px; }
  .label { position: absolute; background: var(--ink); color: var(--paper); overflow: hidden; }
  .label--color { left: 63px; top: 87px; width: 773px; height: 206px; }
  .label--base { left: 63px; top: 359px; width: 773px; height: 206px; }
  .label--remover { left: 30px; top: 650px; width: 841px; height: 456px; }

  .pattern-field { position: absolute; left: 0; top: 0; width: 354px; height: 206px;
    background: linear-gradient(135deg, #2e2e2e, var(--pattern) 50%, #2a2a2a); }

  .front { position: absolute; left: 0; top: 0; width: 354px; height: 206px; text-align: center; }
  .brand-name { font-family: "Barlow", sans-serif; font-weight: 600; color: var(--paper); text-transform: uppercase; line-height: 1; }
  .front .brand-name { position: absolute; left: 0; width: 100%; top: 18px; font-size: 40px; letter-spacing: 5px; }
  .product-line { position: absolute; left: 0; width: 100%; top: 64px; font-family: "Jost", sans-serif; font-size: 21px; line-height: 1; letter-spacing: 0.5px; }
  .product-sub { position: absolute; left: 0; width: 100%; top: 87px; font-family: "Jost", sans-serif; font-size: 13.5px; letter-spacing: 1.5px; line-height: 1; }
  .badge { position: absolute; left: 0; top: 112px; width: 354px; height: 62px; }
  .vegan { position: absolute; left: 0; width: 100%; top: 174px; font-family: "Barlow", sans-serif; font-weight: 700; font-size: 15px; letter-spacing: 0.4px; }

  .copy { position: absolute; left: 420px; top: 18px; width: 281px; font-family: "Barlow Condensed", sans-serif; font-size: 8.8px; line-height: 1.06; text-align: justify; }
  .copy p { margin-bottom: 2px; }
  .copy .lead { font-weight: 600; }
  .label--base .copy .lead { color: var(--rose); font-weight: 500; }
  .copy .rule { height: 1px; background: var(--paper); margin: 4px 14px 4px 0; }
  .label--base .copy .rule { background: var(--rose); }
  .maker { position: absolute; left: 420px; top: 162px; font-family: "Jost", sans-serif; }
  .maker .origin { font-size: 10.5px; font-weight: 500; margin-bottom: 2px; }
  .maker .company { font-size: 8.3px; font-weight: 300; line-height: 1.05; }
  .icons { position: absolute; left: 600px; top: 150px; width: 102px; height: 22px; }
  .volume { position: absolute; left: 618px; top: 180px; font-family: "Barlow", sans-serif; font-weight: 600; font-size: 11px; }
  .label--base .volume { color: var(--rose); }

  .remover-front { position: absolute; left: 0; top: 0; width: 366px; height: 456px; text-align: center; }
  .remover-front .brand-name { position: absolute; left: 0; width: 100%; top: 66px; font-size: 48px; letter-spacing: 6px; }
  .remover-title { position: absolute; left: 0; width: 100%; top: 140px; font-family: "Jost", sans-serif; font-size: 29px; line-height: 42px; letter-spacing: 0.5px; }
  .remover-emblem { position: absolute; left: 103px; top: 270px; width: 160px; height: 125px; }
  .remover-volume { position: absolute; left: 0; width: 100%; top: 408px; font-family: "Barlow", sans-serif; font-weight: 600; font-size: 14px; color: var(--rose); }

  .remover-copy { position: absolute; left: 456px; top: 20px; width: 316px; font-family: "Barlow", sans-serif; font-weight: 400; font-size: 11.6px; line-height: 1.07; text-align: justify; }
  .remover-copy .lead { font-family: "Jost", sans-serif; font-weight: 400; color: var(--rose); font-size: 14px; margin-right: 3px; }
  .remover-copy p { margin-bottom: 3px; text-align: justify; }
  .remover-copy .plain { text-align: left; }
  .remover-copy .rule { height: 1.5px; background: var(--rose); margin: 7px 18px 9px 17px; }
  .remover-footer { position: absolute; left: 456px; top: 336px; width: 316px; text-align: center; font-family: "Jost", sans-serif; font-weight: 300; font-size: 12.5px; line-height: 1.25; }
  .remover-icons { display: block; margin: 6px auto 0; width: 80px; height: 30px; }
  .site { margin-top: 8px; font-family: "Barlow", sans-serif; font-weight: 600; font-size: 14px; color: var(--rose); }
</style>
</head>
<body>
<div class="canvas">

  <section class="label label--color">
    <div class="pattern-field" role="img" aria-label="Dark grey repeating leaf pattern background"></div>
    <div class="front">
      <div class="brand-name">Solvind</div>
      <div class="product-line">COLOR COAT</div>
      <div class="product-sub">SOAK OFF UV/LED</div>
      <svg class="badge" viewBox="0 0 354 62" aria-label="Shade 21, Warm Ember">
        <rect x="133" y="12" width="12" height="12" rx="3" fill="#fff" role="img" aria-label="leaf ornament"/>
        <rect x="209" y="12" width="12" height="12" rx="3" fill="#fff" role="img" aria-label="leaf ornament"/>
        <path d="M157 2 L167 6 L177 2 L187 6 L197 2 L197 26 Q197 34 189 34 L165 34 Q157 34 157 26 Z" fill="var(--red)"/>
        <text x="177" y="29" text-anchor="middle" font-family="Jost, sans-serif" font-size="22" fill="#fff">21</text>
        <path d="M53 34 H110 Q112 34 112 40 V58 H62 Q53 58 53 50 Z" fill="var(--red)"/>
        <path d="M242 34 H300 V50 Q300 58 291 58 H242 Z" fill="var(--red)"/>
        <rect x="118" y="36" width="118" height="22" rx="6" fill="var(--red)"/>
        <text x="177" y="53" text-anchor="middle" font-family="Barlow, sans-serif" font-weight="700" font-size="14" fill="#fff">WARM EMBER</text>
      </svg>
      <div class="vegan">Vegan Formula</div>
    </div>
    <div class="copy">
      <p><span class="lead">DIRECTIONS FOR USE (ENG)</span> Solvind Color Coat must be applied in thin layers and cured in one of our Solvind Lamps.</p>
      <p><span class="lead">ANVENDELSE (DK)</span> Solvind Farver skal påføres i tynde lag og hærdes i en af vores Solvind Lamper.</p>
      <div class="rule"></div>
      <p><span class="lead">CAUTION (ENG)</span> Keep out of reach of children. Discontinue use if irritation occurs. Avoid direct sunlight or extreme exposure to LED or UV light.</p>
      <p><span class="lead">ADVARSEL (DK)</span> Opbevar utilgængeligt for børn. Stop din behandling, hvis produktet forudsager irritation. Undgå direkte sollys eller udsættelse for LED eller UV.</p>
      <div class="rule"></div>
      <p><span class="lead">INGREDIENTS</span> Acrylates Copolymer, Acrylated Aliphatic Urethane, Cellulose Acetate Butanoate, Dimethicone, Ceresine, wax, Pigment Red, Carbon Black, Titanium dioxide, CI 77891</p>
    </div>
    <div class="maker">
      <div class="origin">Made in Europe</div>
      <div class="company">Nordhavn Partners A/S<br>Strandvejen 12 2900 Hellerup, Denmark</div>
    </div>
    <svg class="icons" viewBox="0 0 102 22" fill="none" stroke="#fff" stroke-width="1.6" role="img" aria-label="Hazard, recycle, 24 month and bottle symbols">
      <path d="M11 1 L21 11 L11 21 L1 11 Z" fill="#fff" stroke="var(--red)"/>
      <path d="M11 6 V13 M11 15.5 V16.5" stroke="#000" stroke-width="2"/>
      <circle cx="38" cy="11" r="8"/>
      <path d="M34 13 L38 6 L42 13 Z" fill="#fff"/>
      <rect x="55" y="7" width="18" height="10" rx="2"/>
      <path d="M55 9 H73"/>
      <rect x="88" y="8" width="8" height="12" rx="2"/>
      <path d="M90 8 V2 H94 V8"/>
    </svg>
    <div class="volume">15ml e 0.5oz</div>
  </section>

  <section class="label label--base">
    <div class="front">
      <div class="brand-name">Solvind</div>
      <div class="product-line">BASE COAT</div>
      <div class="product-sub">SOAK OFF UV/LED</div>
      <svg class="badge" viewBox="0 0 354 62" aria-label="Shade 01, Flexible">
        <rect x="133" y="12" width="12" height="12" rx="3" fill="#fff" role="img" aria-label="leaf ornament"/>
        <rect x="209" y="12" width="12" height="12" rx="3" fill="#fff" role="img" aria-label="leaf ornament"/>
        <path d="M157 2 L167 6 L177 2 L187 6 L197 2 L197 26 Q197 34 189 34 L165 34 Q157 34 157 26 Z" fill="var(--rose)"/>
        <text x="177" y="29" text-anchor="middle" font-family="Jost, sans-serif" font-size="22" fill="#000">01</text>
        <path d="M125 34 H245 V50 Q245 58 236 58 H118 V41 Q118 34 125 34 Z" fill="var(--rose)"/>
        <text x="180" y="53" text-anchor="middle" font-family="Barlow, sans-serif" font-weight="700" font-size="14" fill="#000">FLEXIBLE</text>
      </svg>
      <div class="vegan">Vegan Formula</div>
    </div>
    <div class="copy">
      <p><span class="lead">DIRECTIONS FOR USE (ENG)</span> Solvind Base Coat must be applied in thin layers and cured in one of our Solvind Lamps.</p>
      <p><span class="lead">ANVENDELSE (DK)</span> Solvind Base Coat skal påføres i tynde lag og hærdes i en af vores Solvind Lamper.</p>
      <div class="rule"></div>
      <p><span class="lead">CAUTION (ENG)</span> Keep out of reach of children. Discontinue use if irritation occurs. Avoid direct sunlight or extreme exposure to LED or UV Light.</p>
      <p><span class="lead">ADVARSEL (DK)</span> Opbevar utilgængeligt for børn. Stop din behandling, hvis produktet forudsager irritation. Undgå direkte sollys eller udsættelse for LED eller UV.</p>
      <div class="rule"></div>
      <p><span class="lead">INGREDIENTS</span> Acrylates Copolymer, Acrylated Aliphatic Urethane, Cellulose Acetate Butanoate, Dimethicone, Ceresine, wax, Pigment Red, Carbon Black, Titanium dioxide, CI 77891</p>
    </div>
    <div class="maker">
      <div class="origin">Made in Europe</div>
      <div class="company">Nordhavn Partners A/S<br>Strandvejen 12 2900 Hellerup, Denmark</div>
    </div>
    <svg class="icons" viewBox="0 0 102 22" fill="none" stroke="#fff" stroke-width="1.6" role="img" aria-label="Hazard, recycle, 24 month and bottle symbols">
      <path d="M11 1 L21 11 L11 21 L1 11 Z" fill="#fff" stroke="var(--red)"/>
      <path d="M11 6 V13 M11 15.5 V16.5" stroke="#000" stroke-width="2"/>
      <circle cx="38" cy="11" r="8"/>
      <path d="M34 13 L38 6 L42 13 Z" fill="#fff"/>
      <rect x="55" y="7" width="18" height="10" rx="2"/>
      <path d="M55 9 H73"/>
      <rect x="88" y="8" width="8" height="12" rx="2"/>
      <path d="M90 8 V2 H94 V8"/>
    </svg>
    <div class="volume">15ml e 0.5oz</div>
  </section>

  <section class="label label--remover">
    <div class="remover-front">
      <div class="brand-name">Solvind</div>
      <div class="remover-title">GEL POLISH<br>REMOVER</div>
      <svg class="remover-emblem" viewBox="0 0 160 125" aria-label="Shade 21 emblem">
        <rect x="10" y="12" width="24" height="24" rx="6" fill="#fff" role="img" aria-label="leaf ornament"/>
        <rect x="126" y="12" width="24" height="24" rx="6" fill="#fff" role="img" aria-label="leaf ornament"/>
        <path d="M50 2 L65 8 L80 2 L95 8 L110 2 V38 Q110 50 98 50 H62 Q50 50 50 38 Z" fill="var(--rose)"/>
        <text x="80" y="42" text-anchor="middle" font-family="Jost, sans-serif" font-size="30" fill="#000">21</text>
        <rect x="78" y="56" width="4" height="28" fill="#fff"/>
        <rect x="4" y="84" width="38" height="38" rx="10" fill="#fff" role="img" aria-label="leaf ornament"/>
        <rect x="118" y="84" width="38" height="38" rx="10" fill="#fff" role="img" aria-label="leaf ornament"/>
      </svg>
      <div class="remover-volume">120ml e 4fl.oz</div>
    </div>
    <div class="remover-copy">
      <p><span class="lead">DIRECTIONS FOR USE (ENG)</span>To remove the Solvind, soak a lint free wipe with the Solvind Polish Remover, place the saturated wipe on the nail and wrap each nail in foil for 15 minutes. Remove the foil and peel off the gel polish remover. Re-apply if needed. We recommend that you moisturise your nails after this treatment.</p>
      <p><span class="lead">ANVENDELSESGUIDE (DK)</span> For at fjerne Solvind, skal du væde en fnugfri wipe ind i Solvind Neglelakfjerner, hvorefter du placere din fnugfri wipe på neglen og klemmer den fast i 15 minutter med sølvpapir og negleklips. Fjern herefter foliet og skrab din gellak af med en neglebåndsskubber. Gentag hvis nødvendigt. Vi anbefaler negleolie efter din behandling.</p>
      <div class="rule"></div>
      <p class="plain"><span class="lead">CAUTION (ENG)</span>Keep out of the reach of children<br>Discontinue use if sensitivity or irritation occurs</p>
      <p class="plain"><span class="lead">ADVARSEL (DK)</span>Opbevares utilgængeligt for børn<br>Stop din behandling hvis følsomhed eller irritation opstår</p>
      <div class="rule"></div>
      <p class="plain"><span class="lead">INGREDIENTS</span> Ethyl acetate, n-butyl acetate, Methyl Ethyl ketone, Acetone, Isopropyl alcohol, glycerin</p>
    </div>
    <div class="remover-footer">
      Nordhavn Partners A/S<br>Strandvejen 12 2900 Hellerup, Denmark
      <svg class="remover-icons" viewBox="0 0 80 30" fill="none" stroke="#fff" stroke-width="2" role="img" aria-label="Recycle and 24 month symbols">
        <circle cx="16" cy="15" r="12"/>
        <path d="M10 19 L16 8 L22 19 Z" fill="#fff"/>
        <rect x="44" y="8" width="32" height="16" rx="3"/>
        <path d="M44 12 H76"/>
      </svg>
      <div class="site">solvind.com</div>
    </div>
  </section>

</div>
</body>
</html>
```